Business Cards for Orvanta LLC

We need business cards for a new company called “Orvanta LLC”. This is a technology process improvement company providing a comprehensive assessment of the technology used to run their business. The documentation and review process delivers the visibility and reassurance they need to protect their business and plan for the future. The product is called “Systems Mapwork”. Our primary target is small-medium size businesses, with the deliverables going to the decision maker. We would like to see the designs use the color blue. Our tag line is PROTECT YOUR BUSINESS · TAKE CONTROL OF IT.

Industry/Entity Type

Business

Contact Information for Business Card

Tag line should be on back of card - it does not have to be upper case.

Requirements
Must have
• Please use information when laying out card:
• Name: Gareth Pellham
• Title: Partner
• Phone Number: (844)555-0172
• Email: gareth@orvantallc-example.com
• Website: http://orvantallc-example.com

```html
<!DOCTYPE html>
<html lang="en">
<head>
<meta charset="utf-8">
<title>Business Cards for Orvanta LLC</title>
<link rel="stylesheet" href="https://fonts.googleapis.com/css2?family=Open+Sans:wght@400;600;700&display=swap">
<style>
  :root {
    --backdrop: #2a2421;
    --card-white: #ffffff;
    --brand-blue: #2277c8;
    --muted-grey: #8a8a8a;
    --card-grey: #707275;
    --pattern-grey: #7a7c80;
    --text-white: #f4f4f4;
  }
  * { box-sizing: border-box; margin: 0; padding: 0; }
  html, body {
    width: 1200px; height: 900px; overflow: hidden;
    background: var(--backdrop);
    font-family: "Open Sans", Arial, sans-serif;
  }
  .stage { position: relative; width: 1200px; height: 900px; }

  .card {
    position: absolute;
    width: 560px; height: 320px;
    border-radius: 3px;
    box-shadow: 0 12px 30px rgba(0,0,0,.45);
    overflow: hidden;
  }

  /* Front */
  .card-front { left: 50px; top: 470px; background: var(--card-white); }
  .front-brand {
    position: absolute; left: 0; top: 0; width: 290px; height: 320px;
    display: flex; align-items: center; justify-content: center;
  }
  .brand-name {
    font-weight: 700; font-size: 36px; letter-spacing: 1px;
    color: var(--brand-blue);
  }
  .divider {
    position: absolute; left: 292px; top: 80px; width: 1.5px; height: 150px;
    background: var(--brand-blue);
  }
  .contact {
    position: absolute; left: 318px; top: 92px;
    color: var(--brand-blue);
  }
  .contact-name { font-size: 19px; font-weight: 600; line-height: 1.1; }
  .contact-title { font-size: 12px; color: var(--muted-grey); margin: 2px 0 8px; }
  .contact-list { list-style: none; }
  .contact-list li {
    display: flex; align-items: center; gap: 7px;
    font-size: 13.5px; line-height: 22px; white-space: nowrap;
  }
  .contact-list svg { width: 14px; height: 14px; flex: none; }

  /* Back */
  .card-back { left: 600px; top: 150px; background: var(--card-grey); }
  .back-pattern {
    position: absolute; inset: 0;
    background: linear-gradient(160deg, var(--pattern-grey), var(--card-grey));
  }
  .back-brand {
    position: absolute; left: 0; right: 0; top: 100px;
    text-align: center;
  }
  .back-brand .brand-name { color: var(--text-white); font-size: 40px; }
  .tagline {
    position: absolute; left: 0; right: 0; bottom: 34px;
    text-align: center; color: var(--text-white);
    font-size: 13px; font-weight: 600; letter-spacing: 3.2px;
  }
</style>
</head>
<body>
<main class="stage">

  <section class="card card-back" aria-label="Card back">
    <div class="back-pattern" role="img" aria-label="Faint repeated brand monogram pattern"></div>
    <div class="back-brand"><span class="brand-name">Orvanta LLC</span></div>
    <p class="tagline">PROTECT YOUR BUSINESS • TAKE CONTROL OF IT.</p>
  </section>

  <section class="card card-front" aria-label="Card front">
    <div class="front-brand"><span class="brand-name">Orvanta LLC</span></div>
    <div class="divider"></div>
    <div class="contact">
      <p class="contact-name">Gareth Pellham</p>
      <p class="contact-title">Partner</p>
      <ul class="contact-list">
        <li>
          <svg viewBox="0 0 14 14" aria-hidden="true"><rect width="14" height="14" rx="2" fill="#2277c8"/><path d="M4 3.2l1.6-.4.9 2.2-1 .8a5.5 5.5 0 0 0 2.7 2.7l.8-1 2.2.9-.4 1.6c-3.6.3-7.1-3.2-6.8-7z" fill="#fff"/></svg>
          (844)555-0172
        </li>
        <li>
          <svg viewBox="0 0 14 14" aria-hidden="true"><rect width="14" height="14" rx="2" fill="#2277c8"/><rect x="3" y="4.2" width="8" height="5.6" fill="none" stroke="#fff" stroke-width="1"/><path d="M3 4.2l4 3 4-3" fill="none" stroke="#fff" stroke-width="1"/></svg>
          gareth@orvantallc-example.com
        </li>
        <li>
          <svg viewBox="0 0 14 14" aria-hidden="true"><rect width="14" height="14" rx="2" fill="#2277c8"/><circle cx="7" cy="7" r="4" fill="none" stroke="#fff" stroke-width="1"/><ellipse cx="7" cy="7" rx="1.8" ry="4" fill="none" stroke="#fff" stroke-width=".8"/><path d="M3 7h8" stroke="#fff" stroke-width=".8"/></svg>
          orvantallc-example.com
        </li>
      </ul>
    </div>
  </section>

</main>
</body>
</html>
```